Business Card Design

We have recently seen two business cards that caught our attention and think the designs would work for us. We are an accounting firm that serves small businesses in a variety of industries. Attached are the two business card that inspired us along with very rough layouts. We would like to see a professional layout using our company information.

Industry/Entity Type

Accounting

Contact Information for Business Card

Company Name - Dalworth Pryce
Address - 4180 Brambleton Lane, Suite 310, Houston, TX 77051
713-508-9627 - Main
281-369-0714 - Fax

Team Member Names, emails and phone numbers (see attachment)

```html
<!DOCTYPE html>
<html lang="en">
<head>
<meta charset="utf-8">
<title>Dalworth Pryce – Business Card</title>
<link rel="stylesheet" href="https://fonts.googleapis.com/css2?family=Jost:wght@300;400&display=swap">
<style>
  :root {
    --backdrop: #f2f2f2;
    --card: #ffffff;
    --card-edge: #9a9a9a;
    --ink: #1a1a1a;
    --text: #6a6a6a;
    --label: #2a2a2a;
    --mark: #1c1c1c;
  }
  html, body {
    margin: 0;
    padding: 0;
    width: 1200px;
    height: 703px;
    overflow: hidden;
    background: var(--backdrop);
    font-family: "Jost", "Futura", sans-serif;
  }
  .card {
    position: absolute;
    left: 411px;
    top: 39px;
    width: 325px;
    height: 624px;
    box-sizing: border-box;
    background: var(--card);
    border: 1px solid var(--card-edge);
  }
  .brand-square {
    position: absolute;
    left: 128px;
    top: 60px;
    width: 68px;
    height: 68px;
    background: var(--mark);
  }
  .brand-name {
    position: absolute;
    left: 0;
    right: 0;
    top: 176px;
    margin: 0;
    text-align: center;
    font-weight: 400;
    font-size: 19px;
    letter-spacing: 2.4px;
    color: var(--ink);
    line-height: 1;
  }
  .details {
    position: absolute;
    left: 31px;
    color: var(--text);
    font-weight: 300;
    line-height: 1;
  }
  .person-name { top: 324px; font-size: 19px; }
  .person-title { top: 349px; font-size: 14px; }
  .line { font-size: 16.5px; }
  .line .label {
    display: inline-block;
    width: 17px;
    font-size: 12px;
    font-weight: 400;
    color: var(--label);
  }
  .direct { top: 371px; }
  .mobile { top: 393px; }
  .street { top: 452px; font-size: 16.5px; }
  .city { top: 475px; font-size: 16.5px; }
  .main { top: 498px; }
  .fax { top: 521px; }
  .email { top: 574px; font-size: 15.5px; }
</style>
</head>
<body>
  <article class="card">
    <div class="brand-square" aria-hidden="true"></div>
    <h1 class="brand-name">DALWORTH PRYCE</h1>

    <div class="details person-name">Marisol Vantreese</div>
    <div class="details person-title">Account Manager</div>
    <div class="details line direct"><span class="label">T</span>713 . 557 . 2148</div>
    <div class="details line mobile"><span class="label">M</span>832 . 610 . 4793</div>

    <div class="details street">4180 Brambleton Lane, Suite 310</div>
    <div class="details city">Houston, TX 77051</div>
    <div class="details line main"><span class="label">T</span>713 . 508 . 9627</div>
    <div class="details line fax"><span class="label">F</span>281 . 369 . 0714</div>

    <div class="details email">mvantreese@dalworthpryce.com</div>
  </article>
</body>
</html>
```